Looking for a professional, clean and crisp business card

I am in the underground utilities industry and am just looking for a really impressive business card. I would like our card to be white with our symbol crisp and clear with it protruding. I also have a business partner that will require his name and info on the card once the design is set. I would like to have our website info on the card which is;
http://granitetrenchco.example/

Contact Information for Business Card

Website, contact name, number and email

```html
<!DOCTYPE html>
<html lang="en">
<head>
<meta charset="UTF-8">
<title>Granite Trench Co — Business Card</title>
<link href="https://fonts.googleapis.com/css2?family=Archivo:ital,wght@0,400;0,700;1,700&family=Roboto:wght@400&display=swap" rel="stylesheet">
<style>
  :root {
    --card-bg: #ffffff;
    --ink: #000000;
  }
  * { margin: 0; padding: 0; box-sizing: border-box; }
  html, body {
    width: 1200px;
    height: 686px;
    overflow: hidden;
    background: var(--card-bg);
  }
  .card {
    position: relative;
    width: 1200px;
    height: 686px;
    background: var(--card-bg);
    color: var(--ink);
  }
  .brand {
    position: absolute;
    left: 98px;
    top: 130px;
    width: 426px;
    height: 426px;
    border: 14px solid var(--ink);
    border-radius: 50%;
    display: flex;
    align-items: center;
    justify-content: center;
  }
  .brand-name {
    font-family: "Archivo", Arial, sans-serif;
    font-weight: 700;
    font-size: 56px;
    color: var(--ink);
    text-align: center;
    line-height: 1.1;
  }
  .contact {
    position: absolute;
    right: 50px;
    top: 250px;
    text-align: right;
    width: 600px;
  }
  .contact-name {
    font-family: "Archivo", Arial, sans-serif;
    font-weight: 700;
    font-size: 62px;
    line-height: 1;
    letter-spacing: -0.5px;
  }
  .contact-role {
    font-family: "Archivo", Arial, sans-serif;
    font-weight: 700;
    font-size: 40px;
    line-height: 1;
    margin-top: 30px;
  }
  .contact-email,
  .contact-phone {
    font-family: "Roboto", Arial, sans-serif;
    font-weight: 400;
    font-size: 35px;
    line-height: 1;
    letter-spacing: -0.5px;
  }
  .contact-email { margin-top: 18px; }
  .contact-phone { margin-top: 17px; }
  .divider {
    position: absolute;
    left: 672px;
    top: 504px;
    width: 478px;
    height: 19px;
    background: var(--ink);
    border-radius: 9px;
  }
  .website {
    position: absolute;
    right: 50px;
    top: 562px;
    font-family: "Archivo", Arial, sans-serif;
    font-weight: 700;
    font-style: italic;
    font-size: 37px;
    line-height: 1;
  }
</style>
</head>
<body>
  <main class="card">
    <div class="brand">
      <span class="brand-name">Granite<br>Trench Co</span>
    </div>

    <div class="contact">
      <p class="contact-name">Dale Marrick</p>
      <p class="contact-role">Owner</p>
      <p class="contact-email">Dale@granitetrenchco.example</p>
      <p class="contact-phone">250-555-0193(DIGS)</p>
    </div>

    <div class="divider" aria-hidden="true"></div>

    <p class="website">www.granitetrenchco.example</p>
  </main>
</body>
</html>
```